Gestalten Sie ein tolles Selbstliebe-Buchcover
Hallo,
schön, dass Sie sich für diese Ausschreibung interessieren. Wir suchen ein Cover für unser Buch, das wir im Selbstverlag veröffentlichen werden.
Titel: Sanfte Wege ins Morgenlicht
Untertitel 1: Wie du dich von negativen Gedanken befreist und eine liebevolle Beziehung zu dir selbst aufbaust
Untertitel Teil 2: 12 lebensverändernde Monate voller positiver Impulse und Liebe für dich
Das Buch soll (mehrheitlich) Frauen unterstützen, eine liebevolle Beziehung zu sich selbst aufzubauen, negative Gedanken loszulassen und innere Ruhe zu finden.
Aufgabenstellung
Wir sind für jegliche Vorschläge im Rahmen des Themas, der Samples und der Schieberegler offen.
Wichtig ist allerdings
- dass das Design selbst in der kleinen Ansicht (Suchergebnisse) auf Kaufmondo klar hervorsticht, das heißt dort klar erkennbar und die Schrift sofort lesbar ist. Es muss in klein „wirken“, weil viele mit dem Handy auf Kaufmondo shoppen und die Ansicht in den Suchergebnissen dort noch kleiner ist.
- dass das Design die gezielt Emotionen vermittelt
Optimal wäre es, wenn Ihr keine Mockups hochladet. Das macht es viel schwieriger, die Designs einzuschätzen und miteinander zu vergleichen.

```html
<!DOCTYPE html>
<html lang="de">
<head>
<meta charset="utf-8">
<title>Sanfte Wege ins Morgenlicht – Buchcover</title>
<link rel="stylesheet" href="https://fonts.googleapis.com/css2?family=Lato:wght@300;400;700;900&display=swap">
<style>
  :root {
    --paper: #ffffff;
    --title-red: #c1133f;
    --ink: #3a3a3a;
    --author: #ffffff;
    --art-deep: #e13862;
    --art-mid: #e8537f;
    --art-soft: #ee8c9e;
  }
  html, body {
    margin: 0;
    padding: 0;
    overflow: hidden;
    background: var(--paper);
  }
  .cover {
    position: relative;
    width: 846px;
    height: 1200px;
    background: var(--paper);
    overflow: hidden;
    font-family: "Lato", sans-serif;
  }
  .cover__artwork {
    position: absolute;
    top: 0;
    left: 0;
    width: 846px;
    height: 548px;
    background: linear-gradient(120deg, var(--art-deep) 0%, var(--art-mid) 55%, var(--art-soft) 100%);
  }
  .cover__author {
    position: absolute;
    top: 70px;
    left: 0;
    width: 846px;
    padding-left: 295px;
    box-sizing: border-box;
    margin: 0;
    font-weight: 900;
    font-size: 31px;
    letter-spacing: 3px;
    color: var(--author);
  }
  .cover__title {
    position: absolute;
    top: 620px;
    left: 0;
    width: 846px;
    height: 210px;
    margin: 0;
  }
  .cover__title text {
    font-family: "Lato", sans-serif;
    fill: var(--title-red);
  }
  .cover__title .title-main { font-weight: 900; }
  .cover__title .title-sub { font-weight: 300; }
  .cover__subtitle {
    position: absolute;
    top: 855px;
    left: 0;
    width: 846px;
    margin: 0;
    text-align: center;
    font-weight: 300;
    font-size: 31.5px;
    line-height: 40px;
    color: var(--ink);
  }
  .cover__tagline {
    position: absolute;
    top: 1069px;
    left: 0;
    width: 846px;
    margin: 0;
    text-align: center;
    font-weight: 700;
    font-size: 27.5px;
    line-height: 37px;
    text-transform: uppercase;
    color: var(--ink);
  }
</style>
</head>
<body>
<main class="cover">
  <div class="cover__artwork" role="img" aria-label="Abstrakte, weich fließende Farbflächen in Pink- und Rosatönen"></div>

  <p class="cover__author">NAME AUTOR*IN</p>

  <svg class="cover__title" viewBox="0 0 846 210" role="heading" aria-level="1" aria-label="Sanfte Wege ins Morgenlicht">
    <text class="title-main" x="73" y="98" font-size="124" textLength="700" lengthAdjust="spacingAndGlyphs">SANFTE WEGE</text>
    <text class="title-sub" x="78" y="201" font-size="92" textLength="695" lengthAdjust="spacingAndGlyphs">INS MORGENLICHT</text>
  </svg>

  <p class="cover__subtitle">Wie du dich von negativen Gedanken befreist und<br>eine liebevolle Beziehung zu dir selbst aufbaust</p>

  <p class="cover__tagline">12 lebensverändernde Monate voller<br>positiver Impulse und Liebe für dich</p>
</main>
</body>
</html>
```